Seed Oil Safety Card for Healthy Restaurant Dining

I am seeking a design for a physical card to communicate my wife's health-related dietary restriction regarding seed oils. This card will be given to restaurant waiters to ensure her meals are prepared without seed oils, as it is a health issue and not merely a preference.
My wife cannot eat any “seed oil” or “processed oil”, including:
- Vegetable oil
- Canola oil
- Soybean oil
- Sunflower oil
- Corn oil
- Cottonseed oil
- Safflower oil
- Peanut oil
- Sesame oil
Oils that are OK for her to consume:
- Butter (most preferable)
- Extra virgin olive oil
- Avocado oil
- Coconut oil
- Ghee
- Lard
- Any other animal-based fats
Key Design Requirements:
- Clarity and speed of communication: The card should be easily read and understood by waiters, even in low-light environments, emphasizing that it's a health concern.
- Avoid common misconceptions: Ensure the design doesn't imply common dietary preferences like "vegetarian" or "no butter." Animal fats and butter are actually preferable for her!
- Preferred term: Use "seed oils" as the term to describe what she cannot eat due to her health issue.
- Trace amounts are acceptable: Communicate that it's OK to use cookware that has previously been in contact with seed oils, but not to have seed oil as an ingredient. Please suggest a concise way to convey this.
- Card dimensions: Design should be 3.5” x 2.25” (standard credit-card size on cardlora-print.test). Horizontal or vertical layouts are both fine, whichever makes the message clearer.
Design Suggestions:
- Utilize bold and easy-to-read typography to communicate the main message.
- Consider incorporating relevant icons or graphics that help convey the message without adding confusion.
- Use contrasting colors to enhance readability, especially in low-light situations.
- To communicate the “trace amounts OK” part, consider phrases such as:
- "Cross-contamination acceptable"
- “Used cookware OK, no ingredient use”
- “Separate cookware not necessary”
Thank you for your assistance in creating this essential card for my wife's health and safety when dining out!

```html
<!DOCTYPE html>
<html lang="en">
<head>
<meta charset="utf-8">
<title>Dietary Restriction Card – Seed Oils</title>
<link href="https://fonts.googleapis.com/css2?family=Arimo:ital,wght@0,400;0,700;1,400&display=swap" rel="stylesheet">
<style>
  :root {
    --navy: #2b3585;
    --red: #d0202a;
    --green: #3aa335;
    --ok-green: #12a012;
    --yellow: #fbd20c;
    --ink: #111111;
    --grey: #7b7b7b;
    --paper: #ffffff;
  }
  * { margin: 0; padding: 0; box-sizing: border-box; }
  html, body { width: 1200px; height: 771px; overflow: hidden; background: var(--paper); }
  body { font-family: "Arimo", Arial, sans-serif; color: var(--ink); }
  .card { position: relative; width: 1200px; height: 771px; background: var(--paper); overflow: hidden; }

  .title-bar {
    position: absolute; left: 40px; top: 28px; width: 1123px; height: 43px;
    background: var(--navy); color: var(--paper);
    font-weight: 700; font-size: 38px; letter-spacing: 2.5px;
    text-align: right; padding-right: 22px; line-height: 45px;
  }

  .lead { position: absolute; left: 37px; font-weight: 700; font-size: 36.5px; line-height: 1; }
  .lead-cannot { top: 89px; }
  .lead-oils { top: 131px; color: var(--ink); }
  .lead-oils .warn { color: var(--red); }
  .lead-ok { top: 402px; font-size: 32.5px; }
  .lead-ok .good { color: var(--green); }

  .oil-box { position: absolute; left: 35px; width: 980px; border: 3px solid; }
  .oil-box.avoid { top: 169px; height: 164px; border-color: var(--red); }
  .oil-box.allowed { top: 444px; height: 191px; border-color: var(--green); }

  .oil-list { position: absolute; list-style: none; font-size: 35px; letter-spacing: 0.6px; line-height: 1; }
  .oil-list li { position: relative; padding-left: 24px; white-space: nowrap; }
  .oil-list li::before {
    content: ""; position: absolute; left: 2px; top: 12px;
    width: 10px; height: 10px; border-radius: 50%;
  }
  .avoid .oil-list { top: 20px; }
  .avoid .oil-list li { height: 48px; }
  .avoid .oil-list li::before { background: var(--red); }
  .allowed .oil-list { top: 13px; }
  .allowed .oil-list li { height: 44px; }
  .allowed .oil-list li::before { background: var(--green); }
  .col-1 { left: 14px; }
  .col-2 { left: 293px; }
  .col-3 { left: 620px; }
  .allowed .col-2 { left: 474px; }
  .note-inline { font-style: italic; font-size: 28px; letter-spacing: 0.3px; }
  .allowed .wrap { padding-left: 10px; }
  .allowed .wrap::before { display: none; }

  .badge { position: absolute; overflow: visible; }
  .badge.no { left: 947px; top: 160px; }
  .badge.yes { left: 905px; top: 420px; }
  .badge.alert { left: 29px; top: 657px; }

  .cookware-rule { position: absolute; left: 132px; top: 682px; width: 809px; height: 3px; background: var(--yellow); }
  .cookware-note {
    position: absolute; left: 146px; top: 696px;
    font-weight: 700; font-size: 32px; color: var(--grey); line-height: 1;
  }
  .thanks {
    position: absolute; left: 970px; top: 678px;
    font-style: italic; font-size: 19.5px; line-height: 29px; text-align: center; width: 168px;
  }
</style>
</head>
<body>
<main class="card">
  <header class="title-bar">DIETARY RESTRICTION</header>

  <p class="lead lead-cannot">PLEASE I CANNOT EAT</p>
  <p class="lead lead-oils"><span class="warn">ANY SEED OIL</span> OR <span class="warn">PROCESSED OIL</span></p>

  <section class="oil-box avoid">
    <ul class="oil-list col-1"><li>Vegetable oil</li><li>Canola oil</li><li>Soybean oil</li></ul>
    <ul class="oil-list col-2"><li>Sunflower oil</li><li>Corn oil</li><li>Cottonseed oil</li></ul>
    <ul class="oil-list col-3"><li>Safflower oil</li><li>Peanut oil</li><li>Sesame oil</li></ul>
  </section>

  <svg class="badge no" width="212" height="212" viewBox="0 0 212 212">
    <defs>
      <radialGradient id="bottleTones" cx="50%" cy="50%" r="55%">
        <stop offset="0" stop-color="#f2e6a0"/>
        <stop offset="0.5" stop-color="#d9c24a"/>
        <stop offset="1" stop-color="#e8e4d6"/>
      </radialGradient>
    </defs>
    <circle cx="106" cy="106" r="92" fill="url(#bottleTones)" role="img" aria-label="Bottles of seed and vegetable oils"/>
    <circle cx="106" cy="106" r="92" fill="none" stroke="#d0202a" stroke-width="17"/>
    <line x1="41" y1="41" x2="171" y2="171" stroke="#d0202a" stroke-width="17"/>
  </svg>

  <p class="lead lead-ok">OILS THAT ARE <span class="good">OK</span> FOR ME TO CONSUME</p>

  <section class="oil-box allowed">
    <ul class="oil-list col-1">
      <li>Butter <span class="note-inline">(most preferable)</span></li>
      <li>Extra virgin olive oil</li>
      <li>Avocado oil</li>
      <li>Coconut oil</li>
    </ul>
    <ul class="oil-list col-2">
      <li>Ghee</li>
      <li>Lard</li>
      <li>Any other</li>
      <li class="wrap">animal-based fats</li>
    </ul>
  </section>

  <svg class="badge yes" width="260" height="240" viewBox="0 0 260 240">
    <defs>
      <radialGradient id="fatTones" cx="55%" cy="50%" r="55%">
        <stop offset="0" stop-color="#f4edc8"/>
        <stop offset="0.55" stop-color="#d8c57a"/>
        <stop offset="1" stop-color="#8a8a4e"/>
      </radialGradient>
    </defs>
    <circle cx="142" cy="114" r="96" fill="url(#fatTones)" role="img" aria-label="Butter, avocado, olive oil and other approved fats"/>
    <circle cx="142" cy="114" r="96" fill="none" stroke="#12a012" stroke-width="17"/>
    <circle cx="57" cy="133" r="38" fill="#12a012"/>
    <polyline points="38,133 51,147 76,119" fill="none" stroke="#ffffff" stroke-width="10" stroke-linecap="round" stroke-linejoin="round"/>
  </svg>

  <svg class="badge alert" width="92" height="92" viewBox="0 0 92 92" aria-hidden="true">
    <circle cx="46" cy="46" r="44" fill="#fbd20c"/>
    <rect x="39" y="16" width="14" height="40" rx="7" fill="#ffffff"/>
    <circle cx="46" cy="70" r="8" fill="#ffffff"/>
  </svg>
  <div class="cookware-rule"></div>
  <p class="cookware-note">USED COOKWARE OK, NO INGREDIENT USE</p>
  <p class="thanks">Thank you for you cooperation</p>
</main>
</body>
</html>
```